Velvet Pressings Techno Label Business Card

I'm looking for a very clean business card for my Velvet Pressings music label. The label focusses on techno music. The card should include:

• my name : Daniel Hovind as "Founder & CEO"
• email address: daniel@velvet-pressings.net
• web: www.velvet-pressings.net
• facebook logo + /velvetprs
• twitter logo + /velvetprs
• soundcloud logo + /velvetpressings

Feel free to include your ideas! I'm looking forward to discuss about it.

Daniel

Industry/Entity Type

Business

Contact Information for Business Card

I don't like glossy cards. Prefer matt.

Requirements
Nice to have
• Maybe on one side the complete logo, other side just the icon.
Should not have
• Flashy stuff. Must be clean and business like style.

```html
<!DOCTYPE html>
<html lang="en">
<head>
<meta charset="utf-8">
<title>Velvet Pressings – Business Card</title>
<link rel="stylesheet" href="https://fonts.googleapis.com/css2?family=Lato:ital,wght@0,300;0,400;0,700;1,400&display=swap">
<style>
  :root {
    --backdrop: #3b3b3d;
    --card: #0b0b0b;
    --accent: #f07a1e;
    --muted: #8d8d8d;
    --light: #b9b9b9;
  }
  * { box-sizing: border-box; margin: 0; padding: 0; }
  html, body {
    width: 1200px;
    height: 795px;
    overflow: hidden;
    background: var(--backdrop);
    font-family: "Lato", sans-serif;
  }
  .stage {
    position: relative;
    width: 1200px;
    height: 795px;
  }
  .card {
    position: absolute;
    top: 252px;
    width: 500px;
    height: 290px;
    background: var(--card);
    box-shadow: 0 10px 24px rgba(0, 0, 0, 0.45);
  }
  .card--back { left: 60px; }
  .card--front { left: 640px; }

  /* Back side: identity and contact */
  .identity {
    position: absolute;
    top: 96px;
    right: 318px;
    text-align: left;
  }
  .identity__name {
    color: var(--accent);
    font-weight: 700;
    font-size: 17px;
    line-height: 1.1;
  }
  .identity__role {
    color: var(--muted);
    font-weight: 400;
    font-size: 14px;
    line-height: 1.3;
  }
  .divider {
    position: absolute;
    left: 192px;
    top: 96px;
    width: 1.5px;
    height: 102px;
    background: var(--accent);
  }
  .contact-list {
    position: absolute;
    left: 204px;
    top: 96px;
    list-style: none;
  }
  .contact-list__item {
    display: flex;
    align-items: center;
    height: 17px;
    color: var(--light);
    font-size: 13px;
    font-weight: 400;
    letter-spacing: 0.2px;
  }
  .contact-list__icon {
    width: 11px;
    height: 11px;
    margin-right: 9px;
    flex: none;
  }
  .contact-list__marker {
    width: 10px;
    height: 10px;
    margin-right: 10px;
    border-radius: 2px;
    background: var(--accent);
    flex: none;
  }

  /* Front side: wordmark */
  .wordmark {
    position: absolute;
    inset: 0;
    display: flex;
    align-items: center;
    justify-content: center;
    gap: 14px;
  }
  .wordmark__dot {
    width: 40px;
    height: 40px;
    border-radius: 50%;
    background: var(--accent);
  }
  .wordmark__name {
    color: var(--accent);
    font-weight: 700;
    font-size: 38px;
    letter-spacing: -0.5px;
  }
</style>
</head>
<body>
<main class="stage">
  <section class="card card--back" aria-label="Business card, contact side">
    <div class="identity">
      <p class="identity__name">Daniel Hovind</p>
      <p class="identity__role">Founder &amp; CEO</p>
    </div>
    <div class="divider"></div>
    <ul class="contact-list">
      <li class="contact-list__item">
        <svg class="contact-list__icon" viewBox="0 0 12 12" aria-hidden="true">
          <path fill="#f07a1e" d="M2.4 1h2l1 2.6-1.3 1a6.5 6.5 0 0 0 3.3 3.3l1-1.3 2.6 1v2c0 .7-.5 1.2-1.2 1.2A9.6 9.6 0 0 1 1.2 2.2C1.2 1.5 1.7 1 2.4 1z"/>
        </svg>+31640271958
      </li>
      <li class="contact-list__item">
        <svg class="contact-list__icon" viewBox="0 0 12 12" aria-hidden="true">
          <rect x="0.5" y="2" width="11" height="8" rx="1" fill="#f07a1e"/>
          <path d="M1 2.6 6 6.6l5-4" fill="none" stroke="#0b0b0b" stroke-width="1"/>
        </svg>daniel@velvet-pressings.net
      </li>
      <li class="contact-list__item">
        <svg class="contact-list__icon" viewBox="0 0 12 12" aria-hidden="true">
          <circle cx="6" cy="6" r="5.2" fill="none" stroke="#f07a1e" stroke-width="1.2"/>
          <ellipse cx="6" cy="6" rx="2.2" ry="5.2" fill="none" stroke="#f07a1e" stroke-width="1"/>
          <path d="M0.8 6h10.4M1.6 3.4h8.8M1.6 8.6h8.8" stroke="#f07a1e" stroke-width="0.9"/>
        </svg>www.velvet-pressings.net
      </li>
      <li class="contact-list__item"><span class="contact-list__marker"></span>/velvetprs</li>
      <li class="contact-list__item"><span class="contact-list__marker"></span>/velvetprs</li>
      <li class="contact-list__item"><span class="contact-list__marker"></span>/velvetpressings</li>
    </ul>
  </section>

  <section class="card card--front" aria-label="Business card, logo side">
    <div class="wordmark">
      <span class="wordmark__dot"></span>
      <span class="wordmark__name">Velvet Pressings</span>
    </div>
  </section>
</main>
</body>
</html>
```